Banner Ad Design Project

I need a nice banner ad for my company. I do IT development and IT Consulting. The banner should contain my company Logo (see my website www.brimtora.net) and should use the colors from my website (www.brimtora.net). The final design should communicate trust, creativity and competence. It would by nice, when the banner has some animation effects.

Target Market(s)

Manager, IT Directors, IT Decider, HR Manager, Business People

Industry/Entity Type

It Company

Requirements
Must have
• Use my company logo
Use my colors from my website
Technology oriented
Serious but not boring
Some animation
Should not have
• Sound

```html
<!DOCTYPE html>
<html lang="en">
<head>
<meta charset="utf-8">
<title>Brimtora Banner Set</title>
<link rel="stylesheet" href="https://fonts.googleapis.com/css2?family=Arimo:wght@400;700&display=swap">
<style>
  :root {
    --page-bg: #ffffff;
    --gold-light: #f3c93a;
    --gold-mid: #ebb828;
    --gold-dark: #dea21b;
    --gold-text: #d9a21e;
    --panel-white: #ffffff;
    --frame-grey: #b9b9b9;
    --chevron-line: #f6d66a;
    --banner-text: #ffffff;
    --button-top: #5aa3e8;
    --button-bottom: #1159b0;
    --button-edge: #0b3f80;
  }
  * { margin: 0; padding: 0; box-sizing: border-box; }
  html, body { width: 1200px; height: 900px; overflow: hidden; background: var(--page-bg); }
  .canvas { position: relative; width: 1200px; height: 900px; font-family: "Arimo", Arial, sans-serif; }

  .banner {
    position: absolute; left: 136px; width: 924px; height: 100px;
    border-radius: 8px; border: 2px solid var(--frame-grey);
    background: linear-gradient(180deg, var(--gold-light) 0%, var(--gold-mid) 50%, var(--gold-dark) 100%);
    box-shadow: 0 4px 6px rgba(0,0,0,0.22);
    overflow: hidden;
  }
  .banner--consulting { top: 104px; }
  .banner--technology { top: 298px; }
  .banner--development { top: 492px; }
  .banner--learn { top: 686px; }

  .banner__panel { position: absolute; left: 0; top: 0; width: 260px; height: 96px; }

  .brand {
    position: absolute; left: 10px; top: 0; width: 180px; height: 96px;
    display: flex; flex-direction: column; align-items: center; justify-content: center; gap: 6px;
  }
  .brand__dot { width: 30px; height: 30px; border-radius: 50%; background: var(--gold-text); }
  .brand__name { font-size: 24px; font-weight: 400; color: var(--gold-text); letter-spacing: -0.3px; }

  .banner__headline {
    position: absolute; left: 240px; right: 8px; top: 0; height: 96px;
    display: flex; align-items: center; justify-content: center;
    color: var(--banner-text); font-size: 44px; font-weight: 400;
    text-shadow: 0 1px 2px rgba(140,90,0,0.45);
  }

  .banner__tagline {
    position: absolute; left: 258px; top: 0; height: 96px;
    display: flex; align-items: center;
    color: var(--banner-text); font-size: 32px; letter-spacing: 0.5px;
    text-shadow: 0 1px 2px rgba(140,90,0,0.45);
  }
  .cta-button {
    position: absolute; left: 676px; top: 24px; width: 222px; height: 52px;
    border-radius: 6px; border: 2px solid var(--button-edge);
    background: linear-gradient(180deg, var(--button-top) 0%, #2a78cf 48%, var(--button-bottom) 52%, #1a6cc6 100%);
    box-shadow: 0 2px 3px rgba(0,0,0,0.35);
    display: flex; align-items: center; justify-content: center;
    color: var(--banner-text); font-size: 32px; font-weight: 700;
    text-shadow: 0 1px 2px rgba(0,0,0,0.5);
  }
  .cta-button__label { display: inline-block; transform: scaleX(0.88); }
</style>
</head>
<body>
<main class="canvas">

  <section class="banner banner--consulting">
    <svg class="banner__panel" viewBox="0 0 260 96" aria-hidden="true">
      <path d="M0 0 H200 L238 48 L200 96 H0 Z" fill="var(--panel-white)"/>
      <path d="M206 0 L244 48 L206 96" fill="none" stroke="var(--chevron-line)" stroke-width="3"/>
    </svg>
    <div class="brand"><span class="brand__dot"></span><span class="brand__name">brimtora.net</span></div>
    <h2 class="banner__headline">Pallivex Consulting</h2>
  </section>

  <section class="banner banner--technology">
    <svg class="banner__panel" viewBox="0 0 260 96" aria-hidden="true">
      <path d="M0 0 H200 L238 48 L200 96 H0 Z" fill="var(--panel-white)"/>
      <path d="M206 0 L244 48 L206 96" fill="none" stroke="var(--chevron-line)" stroke-width="3"/>
    </svg>
    <div class="brand"><span class="brand__dot"></span><span class="brand__name">brimtora.net</span></div>
    <h2 class="banner__headline">Orvandel Technology</h2>
  </section>

  <section class="banner banner--development">
    <svg class="banner__panel" viewBox="0 0 260 96" aria-hidden="true">
      <path d="M0 0 H200 L238 48 L200 96 H0 Z" fill="var(--panel-white)"/>
      <path d="M206 0 L244 48 L206 96" fill="none" stroke="var(--chevron-line)" stroke-width="3"/>
    </svg>
    <div class="brand"><span class="brand__dot"></span><span class="brand__name">brimtora.net</span></div>
    <h2 class="banner__headline">Software Development</h2>
  </section>

  <section class="banner banner--learn">
    <svg class="banner__panel" viewBox="0 0 260 96" aria-hidden="true">
      <path d="M0 0 H200 L238 48 L200 96 H0 Z" fill="var(--panel-white)"/>
      <path d="M206 0 L244 48 L206 96" fill="none" stroke="var(--chevron-line)" stroke-width="3"/>
    </svg>
    <div class="brand"><span class="brand__dot"></span><span class="brand__name">brimtora.net</span></div>
    <p class="banner__tagline">LEARN IT - SHARE IT</p>
    <span class="cta-button"><span class="cta-button__label">Click Here</span></span>
  </section>

</main>
</body>
</html>
```